Education / Investment Website Design (PDF Wireframe Provided)

More details are in the wireframe document

We need a website design for an investment education company. Our Clients purchase education courses through us. We use meridian toolkit (Wordpress) for our website. We just require the graphics in PSD (not coded) for the

1. Homepage - brightfunnelhub.com style
2. Blog page - brightfunnelhub.com style
3. Single Blog Post
4. Product page - Lernova.com style
5. Single Product Page - https://www.lernova.com/share-market-class-oceania/?ref=kP7qLmW3xT9Z
6. Contact Us Page (Contact Us Form, Map and Contact details)
7. About Us Page

See the attached Wireframe for the homepage

IMPORTANT
Websites we like are clean, white, similar to BrightFunnelHub.com and Lernova.com
Use of white space, big fonts, flat buttons

Attached wireframe is the flow of the homepage. (Homepage brief PDF)

Each section represents a "fold" as visitors are scrolling down. (Homepage showing folds PDF - how the visitor sees each section of the homepage as they scroll down the homepage)

We've got a clear idea of the elements on the page and looking for a great graphic / web designer to create those for us. (We do the coding)

Website currently is: southerncrosswealthschool.com.au (we want to simplify the website and have a more modern / flat design)

Questions: Please ask

Target Market(s)

Investors, People looking for Investment / Financial Education

Industry/Entity Type

Investment

Number of Pages Required

5+ page

Font styles to use
Sans Serif

Requirements
Must have
• Similar Items listed in the wireframe
• Clean Look - Flat design - elegant
• Roll-over (mouse on / mouse off) for Buttons and Top Banner Selection
Should not have
• Images that looks too much like "Stock Images"
• Please avoid bright orange

```html
<!DOCTYPE html>
<html lang="en">
<head>
<meta charset="utf-8">
<title>Southern Cross Wealth School — Home</title>
<link rel="stylesheet" href="https://fonts.googleapis.com/css2?family=Cabin:wght@400;500&family=Lato:wght@300;400;700&family=Montserrat:wght@400;500&display=swap">
<style>
  :root {
    --topbar: #5e5e5e;
    --search: #8c8c8c;
    --hero-light: #a9e2e0;
    --hero-mid: #86cfd0;
    --hero-deep: #6cc0c6;
    --accent: #0f9692;
    --accent-dark: #0c8784;
    --ink: #333b3f;
    --ink-soft: #555d60;
    --card: #ffffff;
    --card-frost: rgba(255,255,255,0.55);
    --card-edge: #cfd8d8;
    --white: #ffffff;
    --social: rgba(225,230,230,0.85);
  }
  * { box-sizing: border-box; margin: 0; padding: 0; }
  html, body { width: 1200px; height: 900px; overflow: hidden; }
  body { position: relative; font-family: "Lato", sans-serif; background: var(--hero-mid); }

  .top-bar { position: absolute; top: 0; left: 0; width: 1200px; height: 37px; background: var(--topbar); }
  .top-bar__note { position: absolute; left: 161px; top: 10px; font: 500 13px "Montserrat", sans-serif; color: var(--white); }
  .top-bar__search { position: absolute; left: 844px; top: 0; width: 205px; height: 37px; background: var(--search); }
  .top-bar__search span { position: absolute; left: 16px; top: 11px; font: 400 13px "Montserrat", sans-serif; color: #eef0f0; }
  .top-bar__search svg { position: absolute; right: 16px; top: 11px; }

  .hero { position: absolute; top: 37px; left: 0; width: 1200px; height: 863px;
    background: radial-gradient(ellipse at 30% 30%, var(--hero-light), transparent 60%),
                radial-gradient(ellipse at 80% 70%, var(--hero-deep), transparent 65%),
                linear-gradient(160deg, var(--hero-light), var(--hero-mid) 50%, var(--hero-deep)); }

  .account-links { position: absolute; top: 51px; left: 876px; font: 500 12px "Montserrat", sans-serif; color: var(--white); }
  .account-links .sep { margin: 0 5px; }
  .account-links .contact { margin-left: 32px; }

  .brand { position: absolute; left: 135px; top: 63px; display: flex; align-items: center; gap: 10px; }
  .brand__dot { width: 50px; height: 50px; border-radius: 50%; background: #2c3e4a; }
  .brand__name { font: 700 19px "Lato", sans-serif; color: #1f2a33; line-height: 1.05; letter-spacing: 0.5px; }

  .main-nav { position: absolute; top: 99px; left: 674px; display: flex; gap: 26px; font: 500 12px "Montserrat", sans-serif; color: var(--white); letter-spacing: 0.3px; }
  .main-nav .is-active { color: #2a3236; }

  .social { position: absolute; right: 0; top: 181px; }
  .social a { position: absolute; display: flex; align-items: center; justify-content: center; width: 48px; height: 41px; background: var(--social); font: 700 12px "Lato", sans-serif; color: #a3aaab; text-decoration: none; }
  .social a.is-hover { color: var(--accent); }

  .hero__title { position: absolute; top: 282px; left: 0; width: 1190px; text-align: center; font: 400 45px "Cabin", sans-serif; color: var(--ink); letter-spacing: 0.3px; }
  .hero__sub { position: absolute; top: 340px; left: 149px; font: 400 23px "Cabin", sans-serif; color: var(--ink-soft); }

  .service { position: absolute; top: 462px; width: 281px; height: 177px; background: var(--card); border: 2px solid var(--card-edge); display: flex; align-items: center; justify-content: center; text-align: center; padding: 10px 14px 0; font: 300 22px/1.25 "Lato", sans-serif; color: var(--ink-soft); }
  .service--frost { background: var(--card-frost); border-color: rgba(255,255,255,0.6); }
  .service__icon { position: absolute; top: -28px; left: 50%; margin-left: -28px; width: 56px; height: 56px; border-radius: 50%; background: var(--accent); display: flex; align-items: center; justify-content: center; }

  .join-btn { position: absolute; left: 458px; top: 733px; width: 285px; height: 48px; background: var(--accent-dark); color: var(--white); font: 700 14px "Lato", sans-serif; text-transform: uppercase; display: flex; align-items: center; justify-content: center; letter-spacing: -0.2px; text-decoration: none; }
</style>
</head>
<body>
  <header class="top-bar">
    <p class="top-bar__note">First time visitor? Then star here and lear more about Southern Cross Wealth School!</p>
    <div class="top-bar__search">
      <span>Search</span>
      <svg width="14" height="14" viewBox="0 0 14 14"><circle cx="5.5" cy="5.5" r="4" fill="none" stroke="#fff" stroke-width="2"/><line x1="8.5" y1="8.5" x2="13" y2="13" stroke="#fff" stroke-width="2.4"/></svg>
    </div>
  </header>

  <section class="hero" role="img" aria-label="Soft teal photo of a hand touching a screen with a globe, flight paths and shopping cart graphics"></section>

  <nav class="account-links"><a>Sign in</a><span class="sep">|</span><a>Join</a><a class="contact">Contact us</a></nav>

  <div class="brand">
    <span class="brand__dot"></span>
    <span class="brand__name">SOUTHERN CROSS<br>WEALTH SCHOOL</span>
  </div>

  <nav class="main-nav">
    <a class="is-active">HOME</a><a>BLOG</a><a>PRODUCTS</a><a>ABOUT US</a><a>MEMBERS</a>
  </nav>

  <aside class="social">
    <a style="top:0;right:0">FV</a>
    <a class="is-hover" style="top:50px;right:0;width:60px">CL</a>
    <a style="top:101px;right:0">SE</a>
    <a style="top:151px;right:0">VT</a>
  </aside>

  <h1 class="hero__title">EDUCATION. RECOMMENDATIONS. AUTOPILOT</h1>
  <p class="hero__sub">Which investment service do you want to recive today?</p>

  <div class="service" style="left:151px">
    <span class="service__icon"><svg width="26" height="22" viewBox="0 0 26 22"><path d="M1 3 Q7 1 12 4 V21 Q7 18 1 20Z M25 3 Q19 1 14 4 V21 Q19 18 25 20Z" fill="#fff"/></svg></span>
    I want to learn to<br>trade from A — Z
  </div>
  <div class="service service--frost" style="left:460px">
    <span class="service__icon"><svg width="24" height="22" viewBox="0 0 24 22"><rect x="1" y="15" width="4" height="7" fill="#fff"/><rect x="7" y="11" width="4" height="11" fill="#fff"/><rect x="13" y="6" width="4" height="16" fill="#fff"/><rect x="19" y="1" width="4" height="21" fill="#fff"/></svg></span>
    I want to know exactly what OCX and US shares to Trade
  </div>
  <div class="service" style="left:769px">
    <span class="service__icon"><svg width="28" height="22" viewBox="0 0 28 22"><circle cx="7" cy="6" r="3.5" fill="#fff"/><circle cx="21" cy="6" r="3.5" fill="#fff"/><circle cx="14" cy="5" r="4.5" fill="#fff"/><path d="M1 20 Q1 11 7 11 Q13 11 13 20Z M15 20 Q15 11 21 11 Q27 11 27 20Z" fill="#fff"/><path d="M6 21 Q6 11 14 11 Q22 11 22 21Z" fill="#fff"/></svg></span>
    I want to Trading to be on AutoPilot and outsource all the hard work
  </div>

  <a class="join-btn">Join over 20 000 fellow investors</a>
</body>
</html>
```